Need a business card design. I am a Self Empowerment Life Coach.

A Life Coach is - a professional relationship designed to enhance an individual's ability to focus, make effective changes, develop oneself, achieve desired goals and maximize success in life. Coaching is about getting the very best out of someone and enabling them to make decisions that will improve their life. It is a unique way to help people look at where they are now and where they would like to be, and helps bridge the gap.

Tidal Grove Coaching is motivational, inspiring, positive, exciting and action driven. By raising awareness and encouraging others to take responsibility for their life, coaching can help people rise to their challenge and go further than you ever thought possible.

Industry/Entity Type

Business

Font styles to use
Other font styles liked:
• Bookman Old Style

Requirements
Must have
• Marlena Voskuil, ELI-MP
• Self Empowerment Coach
• 358.617.2083
• mv@thebrightpathguide.net
• The attached logo
Nice to have
• I would like to see some designs portrait and some landscape

```html
<!DOCTYPE html>
<html lang="en">
<head>
<meta charset="utf-8">
<title>Tidal Grove Coaching – Business Card</title>
<link rel="stylesheet" href="https://fonts.googleapis.com/css2?family=Raleway:wght@400;500;700&display=swap">
<style>
  :root {
    --page: #ecebe8;
    --card: #ffffff;
    --frame-light: #c9cdcd;
    --frame-teal: #8fa1a0;
    --ink: #111313;
    --band: #0f1212;
    --bar: #8fa1a0;
    --white: #ffffff;
    --muted: #3a3f3f;
    --art-a: #c3c8c8;
    --art-b: #8e9a9a;
  }
  * { box-sizing: border-box; margin: 0; padding: 0; }
  html, body { width: 1057px; height: 1200px; overflow: hidden; }
  body {
    background: var(--page);
    font-family: "Raleway", sans-serif;
    color: var(--ink);
    position: relative;
  }

  .card {
    position: absolute;
    background: var(--card);
    box-shadow: 0 6px 18px rgba(0,0,0,.12);
  }

  /* Front – landscape */
  .card-front {
    left: 168px; top: 70px;
    width: 720px; height: 411px;
    border: 14px solid var(--frame-light);
    display: flex; flex-direction: column;
  }
  .front-head {
    height: 150px;
    display: flex; justify-content: space-between; align-items: center;
    padding: 0 40px;
  }
  .holder-name {
    font-size: 26px; font-weight: 500; letter-spacing: 1.5px;
    text-transform: uppercase;
  }
  .holder-title {
    margin-top: 8px; font-size: 13px; letter-spacing: 2px;
    text-transform: uppercase; color: var(--muted);
  }
  .brand-name {
    text-align: right;
    font-size: 22px; font-weight: 700; text-transform: uppercase;
    letter-spacing: 1px; line-height: 1.1; color: var(--ink);
  }

  .contact-band {
    flex: 1;
    background: var(--band);
    color: var(--white);
    padding: 20px 40px;
    display: flex; flex-direction: column; justify-content: space-between;
  }
  .contact-row { display: flex; align-items: center; gap: 16px; font-size: 15px; letter-spacing: 1px; }
  .icon-box {
    width: 24px; height: 24px; border-radius: 4px;
    background: var(--white);
    display: flex; align-items: center; justify-content: center;
  }
  .icon-box svg { width: 16px; height: 16px; }

  .address-bar {
    height: 46px; background: var(--bar); color: var(--white);
    display: flex; align-items: center; gap: 14px;
    padding: 0 40px; font-size: 14px; letter-spacing: 1px;
  }

  /* Back – portrait */
  .card-back {
    left: 358px; top: 550px;
    width: 340px; height: 595px;
    border: 16px solid var(--frame-teal);
    display: flex; align-items: center; justify-content: center;
  }
  .mascot-art {
    width: 220px; height: 150px; border-radius: 12px;
    background: linear-gradient(180deg, var(--art-a), var(--art-b));
  }
</style>
</head>
<body>

  <section class="card card-front">
    <header class="front-head">
      <div class="holder">
        <h1 class="holder-name">Marlena Voskuil, ELI-MP</h1>
        <p class="holder-title">Self Empowerment Coach</p>
      </div>
      <p class="brand-name">Tidal Grove<br>Coaching</p>
    </header>

    <div class="contact-band">
      <div class="contact-row">
        <span class="icon-box"><svg viewBox="0 0 16 16"><path d="M4 1.5h2l1 3.5-1.5 1a8 8 0 0 0 4.5 4.5l1-1.5 3.5 1v2A1.5 1.5 0 0 1 13 14.5 11.5 11.5 0 0 1 1.5 3 1.5 1.5 0 0 1 4 1.5z" fill="#111313"/></svg></span>
        <span>358.617.2083</span>
      </div>
      <div class="contact-row">
        <span class="icon-box"><svg viewBox="0 0 16 16"><rect x="4" y="1.5" width="8" height="13" rx="1.5" fill="none" stroke="#111313" stroke-width="1.6"/><circle cx="8" cy="12" r="1" fill="#111313"/></svg></span>
        <span>358.617.2090</span>
      </div>
      <div class="contact-row">
        <span class="icon-box"><svg viewBox="0 0 16 16"><rect x="1.5" y="3.5" width="13" height="9" rx="1" fill="none" stroke="#111313" stroke-width="1.5"/><path d="M2 4l6 5 6-5" fill="none" stroke="#111313" stroke-width="1.5"/></svg></span>
        <span>mv@thebrightpathguide.net</span>
      </div>
      <div class="contact-row">
        <span class="icon-box"><svg viewBox="0 0 16 16"><circle cx="8" cy="8" r="6.2" fill="none" stroke="#111313" stroke-width="1.4"/><ellipse cx="8" cy="8" rx="2.6" ry="6.2" fill="none" stroke="#111313" stroke-width="1.2"/><path d="M2 8h12" stroke="#111313" stroke-width="1.2"/></svg></span>
        <span>www.thebrightpathguide.net</span>
      </div>
    </div>

    <footer class="address-bar">
      <span class="icon-box"><svg viewBox="0 0 16 16"><path d="M8 1.5a4.5 4.5 0 0 0-4.5 4.5c0 3.4 4.5 8.5 4.5 8.5s4.5-5.1 4.5-8.5A4.5 4.5 0 0 0 8 1.5z" fill="#8fa1a0"/><circle cx="8" cy="6" r="1.6" fill="#fff"/></svg></span>
      <span>48 Harbor Lane, Suite 3, Maple Ridge</span>
    </footer>
  </section>

  <section class="card card-back">
    <div class="mascot-art" role="img" aria-label="Brand mascot illustration in grey tones"></div>
  </section>

</body>
</html>
```